Rocket business card

Modern business card design, use of color is good with clean space too.

Things to include on card:

Quote: I add fuel to your optometry practice

- Eyewear Sales
- Admin Duties
- Revenue Collection
- Leadership
- Tech Adoption
- COGS Reduction
- Product Sourcing
-Medical Growth

Dalton Vessey, CEO
Glint Harbor
Text Me! 847-302-1964
dalton@glintharbor.example

```html
<!DOCTYPE html>
<html lang="en">
<head>
<meta charset="utf-8">
<title>Glint Harbor Business Card</title>
<link rel="stylesheet" href="https://fonts.googleapis.com/css2?family=Lato:wght@400;700;900&display=swap">
<style>
  :root {
    --sky: #5fc9e6;
    --plum: #8c1840;
    --amber: #f49a22;
    --ink: #111111;
    --paper: #ffffff;
    --backdrop-light: #ebe9ea;
    --backdrop-dark: #b4b3b4;
  }
  * { margin: 0; padding: 0; box-sizing: border-box; }
  html, body { width: 1200px; height: 807px; overflow: hidden; }
  body {
    background: linear-gradient(135deg, var(--backdrop-light) 0%, var(--backdrop-dark) 100%);
    font-family: "Lato", sans-serif;
    position: relative;
  }
  .card {
    position: absolute;
    top: 255px;
    width: 520px;
    height: 297px;
    border-radius: 18px;
    overflow: hidden;
    box-shadow: 0 10px 24px rgba(0,0,0,0.22);
  }
  .card-front { left: 60px; }
  .card-back { left: 620px; }
  .card-art { position: absolute; inset: 0; width: 100%; height: 100%; }

  .brand {
    position: absolute;
    display: flex;
    align-items: center;
    gap: 10px;
    color: var(--ink);
    font-weight: 700;
    letter-spacing: 1px;
    white-space: nowrap;
  }
  .brand-dot {
    width: 34px; height: 34px; border-radius: 50%;
    background: var(--amber);
    flex: none;
  }
  .card-front .brand { left: 34px; top: 38px; font-size: 24px; }

  .holder { position: absolute; left: 34px; top: 104px; color: var(--ink); }
  .holder-name { font-size: 20px; font-weight: 900; }
  .holder-role { font-size: 16px; font-weight: 700; margin-top: 2px; }

  .contact { position: absolute; left: 34px; bottom: 34px; list-style: none; color: var(--ink); font-size: 14px; }
  .contact li { display: flex; align-items: center; gap: 8px; margin-top: 6px; white-space: nowrap; }
  .contact svg { width: 16px; height: 16px; flex: none; }

  .services {
    position: absolute;
    right: 24px; top: 50px;
    list-style: none;
    color: var(--paper);
    font-size: 15px;
    line-height: 1.3;
    text-align: left;
    white-space: nowrap;
  }

  .card-back .brand {
    left: 50%; top: 50%;
    transform: translate(-42%, -50%);
    font-size: 30px;
  }
  .card-back .brand-dot { width: 46px; height: 46px; }
</style>
</head>
<body>

  <section class="card card-front" aria-label="Business card front">
    <svg class="card-art" viewBox="0 0 520 297" preserveAspectRatio="none" aria-hidden="true">
      <rect width="520" height="297" fill="var(--sky)"/>
      <polygon points="330,0 358,0 288,297 260,297" fill="var(--amber)"/>
      <polygon points="358,0 520,0 520,297 288,297" fill="var(--plum)"/>
    </svg>

    <div class="brand"><span class="brand-dot"></span>Glint Harbor</div>

    <div class="holder">
      <p class="holder-name">Dalton Vessey</p>
      <p class="holder-role">CEO Glint Harbor</p>
    </div>

    <ul class="contact">
      <li>
        <svg viewBox="0 0 16 16"><circle cx="8" cy="8" r="7.5" fill="var(--ink)"/><path d="M5.5 4.5l1.6 0 .6 2-1 .8a5 5 0 0 0 2 2l.8-1 2 .6 0 1.6a1 1 0 0 1-1 1A7 7 0 0 1 4.5 5.5a1 1 0 0 1 1-1z" fill="var(--sky)"/></svg>
        <span>847-302-1964</span>
      </li>
      <li>
        <svg viewBox="0 0 16 16"><circle cx="8" cy="8" r="7.5" fill="var(--ink)"/><rect x="4" y="5" width="8" height="6" fill="none" stroke="var(--sky)" stroke-width="1"/><path d="M4 5l4 3.2L12 5" fill="none" stroke="var(--sky)" stroke-width="1"/></svg>
        <span>dalton@glintharbor.example</span>
      </li>
    </ul>

    <ul class="services">
      <li>Eyewear Sales</li>
      <li>Admin Duties</li>
      <li>Revenue Collection</li>
      <li>Leader Ship</li>
      <li>Tech Adoption</li>
      <li>Cogs Reduction</li>
      <li>Product Sourcing</li>
      <li>Medical Growth</li>
    </ul>
  </section>

  <section class="card card-back" aria-label="Business card back">
    <svg class="card-art" viewBox="0 0 520 297" preserveAspectRatio="none" aria-hidden="true">
      <rect width="520" height="297" fill="var(--sky)"/>
      <polygon points="0,0 120,0 0,170" fill="var(--plum)"/>
      <polygon points="120,0 150,0 0,212 0,170" fill="var(--amber)"/>
      <polygon points="520,150 520,297 390,297" fill="var(--plum)"/>
      <polygon points="520,112 520,150 390,297 348,297" fill="var(--amber)"/>
    </svg>
    <div class="brand"><span class="brand-dot"></span>Glint Harbor</div>
  </section>

</body>
</html>
```